I will ask the design of the business card

We are looking for business card design of the new company "TORVIK QUANTA WORKS LLC." Based in Azerbaijan.
In case
We are working on Azerbaijan to set up the first exchange of crypto currencies.

The key currency used in exchanges is called "MELDA".
In case
We are doing project to make crypto currency infrastructure.

We provide state-of-the-art technology to the world.

```html
<!DOCTYPE html>
<html lang="en">
<head>
<meta charset="utf-8">
<title>Torvik Quanta Works LLC – Business Card</title>
<link rel="stylesheet" href="https://fonts.googleapis.com/css2?family=Work+Sans:wght@400;500;600&display=swap">
<style>
  :root {
    --stage: #1d1d1f;
    --card: #232325;
    --card-edge: #2b2b2e;
    --ink: #f2f2f2;
    --accent: #1f78c8;
    --emboss: #4a4a4d;
  }
  * { margin: 0; padding: 0; box-sizing: border-box; }
  html, body {
    width: 1200px; height: 900px; overflow: hidden;
    background: var(--stage);
    font-family: "Work Sans", sans-serif;
  }
  .stage {
    width: 1200px; height: 900px;
    display: flex; flex-direction: column;
    align-items: center; justify-content: center; gap: 40px;
  }
  .card {
    width: 680px; height: 388px;
    background: linear-gradient(135deg, var(--card) 0%, var(--card-edge) 100%);
    box-shadow: 0 18px 40px rgba(0,0,0,.55);
    position: relative;
    overflow: hidden;
  }
  /* Back side */
  .card-back { display: flex; align-items: center; justify-content: center; }
  .brand { display: flex; align-items: center; gap: 10px; }
  .brand-dot { width: 20px; height: 20px; border-radius: 50%; flex: none; }
  .brand-name { font-weight: 400; letter-spacing: .03em; white-space: nowrap; }
  .card-back .brand { gap: 12px; }
  .card-back .brand-dot { background: var(--emboss); width: 30px; height: 30px; }
  .card-back .brand-name { color: var(--emboss); font-size: 30px; letter-spacing: .04em; }

  /* Front side */
  .card-front .brand { position: absolute; left: 40px; top: 114px; width: 284px; }
  .card-front .brand-dot { background: var(--accent); }
  .card-front .brand-name { color: var(--ink); font-size: 16px; }
  .divider {
    position: absolute; left: 342px; top: 108px;
    width: 2px; height: 172px; background: var(--ink);
  }
  .contact { position: absolute; left: 372px; top: 108px; color: var(--ink); }
  .person-name {
    color: var(--accent); font-size: 25px; font-weight: 600;
    letter-spacing: .08em; line-height: 1;
  }
  .person-role { font-size: 14px; margin: 4px 0 16px; }
  .address { font-size: 14px; line-height: 1.35; letter-spacing: .03em; margin-bottom: 10px; }
  .contact-list { list-style: none; font-size: 15px; letter-spacing: .03em; line-height: 1.5; }
  .contact-list li { display: flex; align-items: center; gap: 10px; }
  .contact-list svg { width: 12px; height: 12px; flex: none; }
  .web-domain { color: var(--accent); }
</style>
</head>
<body>
<main class="stage">
  <section class="card card-back" aria-label="Card back">
    <div class="brand">
      <span class="brand-dot"></span>
      <span class="brand-name">TORVIK QUANTA WORKS LLC.</span>
    </div>
  </section>

  <section class="card card-front" aria-label="Card front">
    <div class="brand">
      <span class="brand-dot"></span>
      <span class="brand-name">TORVIK QUANTA WORKS LLC.</span>
    </div>
    <div class="divider"></div>
    <div class="contact">
      <h1 class="person-name">DANIEL ORLEN</h1>
      <p class="person-role">Director</p>
      <p class="address">AZ1010 , 8/3 Nizami str.<br>Baku city, Azerbaijan</p>
      <ul class="contact-list">
        <li>
          <svg viewBox="0 0 12 12" aria-hidden="true"><path d="M3 1 L5 3.5 L4 4.8 C4.6 6 6 7.4 7.2 8 L8.5 7 L11 9 L9.8 11 C6 11 1 6 1 2.2 Z" fill="none" stroke="#1f78c8" stroke-width="1"/></svg>
          555-204-7316
        </li>
        <li>
          <svg viewBox="0 0 12 12" aria-hidden="true"><rect x="1" y="2.5" width="10" height="7" fill="none" stroke="#1f78c8" stroke-width="1"/><path d="M1 2.5 L6 6.5 L11 2.5" fill="none" stroke="#1f78c8" stroke-width="1"/></svg>
          support@melda.technology
        </li>
        <li>
          <svg viewBox="0 0 12 12" aria-hidden="true"><circle cx="6" cy="6" r="5" fill="none" stroke="#1f78c8" stroke-width="1"/><ellipse cx="6" cy="6" rx="2.2" ry="5" fill="none" stroke="#1f78c8" stroke-width="1"/><path d="M1 6 H11" stroke="#1f78c8" stroke-width="1"/></svg>
          <span>www.<span class="web-domain">guild.melda.technology</span></span>
        </li>
      </ul>
    </div>
  </section>
</main>
</body>
</html>
```